B2B EDM Banner Design- Specialist Tech Company

We need a new top-of-email banner for our EDM campaigns for Varnel Brix (www.varnelbrix-example.com
). This banner will sit at the top of every email and must immediately signal the brand, look modern and professional, and be visually aligned with the tech/IT audience.
Size of the banner: Around 728x90 - it must fit at the top of an email blast.
Purpose of the Banner
Establish a strong, recognizable brand identity across all Varnel Brix EDMs
visually consistent with existing banners created for other brands (see reference examples provided)
Communicate Varnel Brix’s value proposition at a glance
Brand Name
Varnel Brix
Tagline (must appear in the banner)
“11,322 whitepapers from 726 companies”
Design Requirements
Style & Tone
Modern, clean, and professional
Tech-centric look and feel
High-quality, sleek, and corporate
Eye-catching but not cluttered
Should feel premium and authoritative
Layout & Composition
Full-width banner for email header
Horizontal orientation similar to the Plomtar and Quindle Staff Archive examples
Include space for the brand name/logo prominently on the left or centered
Integrate the tagline in a readable, secondary position
Optional: a subtle background texture or tech-related abstract pattern (circuitry, network nodes, gradient, etc.)
No busy imagery—should feel clean and trustworthy
Color Palette
Use colors consistent with Varnel Brix branding from www.varnelbrix-example.com
Blues, greys, blacks, and tech-style gradients preferred
Should feel consistent with a B2B IT audience
Typography
Clean, sans-serif fonts (professional/tech-aligned)
Brand name should be bold and prominent
Tagline should be smaller, but still readable on desktop and mobile
Imagery (if used)
Abstract tech shapes, network visuals, geometric patterns, or gradient overlays
Avoid photography of people
Keep imagery subtle so text remains legible
Call-to-Action Button (optional)
None required in this banner (unlike the HR examples)
Banner should remain a pure brand header
Deliverables
Final banner in PNG and JPG formats
2–3 design variations (if possible) for A/B testing
Dimensions optimized for EDM: ~600–700px wide (standard email width), proportionate height

```html
<!DOCTYPE html>
<html lang="en">
<head>
<meta charset="utf-8">
<title>Varnel Brix – EDM Header Banners</title>
<link href="https://fonts.googleapis.com/css2?family=Montserrat:ital,wght@0,500;0,600;0,700;0,800;1,500&family=Oswald:wght@400;500;600&display=swap" rel="stylesheet">
<style>
  :root {
    --stage-light: #e6e6e6;
    --stage-dark: #9a9a9a;
    --ink-black: #050607;
    --brand-blue: #1a9ee0;
    --deep-blue: #0a5f9c;
    --white: #ffffff;
    --paper: #ffffff;
    --text-dark: #0d0d0d;
  }
  * { margin: 0; padding: 0; box-sizing: border-box; }
  html, body { width: 1200px; height: 960px; overflow: hidden; }
  body {
    position: relative;
    background: radial-gradient(ellipse at 50% 110%, var(--stage-light) 0%, #c9c9c9 45%, var(--stage-dark) 100%);
    font-family: "Montserrat", sans-serif;
  }
  .banner {
    position: absolute;
    left: 82px;
    width: 1057px;
    height: 131px;
    overflow: hidden;
    box-shadow: 0 14px 18px -10px rgba(0,0,0,.45);
  }
  .banner--one   { top: 156px; background: var(--ink-black); }
  .banner--two   { top: 327px; background: linear-gradient(100deg, #0d3a5a 0%, #0a1d33 40%, #120f25 60%, #0b3d66 85%, #1a8fd0 100%); }
  .banner--three { top: 510px; background: linear-gradient(100deg, #0a0d1a 0%, #1a1638 25%, #05070c 50%, #0c2a45 80%, #1b6aa0 100%); }
  .banner--four  { top: 683px; background: linear-gradient(100deg, #050505 0%, #0a0d12 45%, #0c2440 75%, #0a0e16 100%); }

  .tech-texture {
    position: absolute; inset: 0;
    background: radial-gradient(ellipse at 20% 30%, rgba(40,110,160,.22), transparent 60%);
  }

  /* Brand lockup */
  .brand { position: absolute; display: flex; align-items: center; gap: 18px; }
  .brand__mark {
    width: 64px; height: 64px; border-radius: 50%;
    background: var(--brand-blue);
    flex: none;
  }
  .brand__text { display: flex; flex-direction: column; }
  .brand__name {
    font-weight: 800; color: var(--white);
    font-size: 31px; line-height: 1; letter-spacing: .5px;
    white-space: nowrap;
  }
  .brand__tagline {
    margin-top: 8px; padding-top: 5px;
    border-top: 1px solid var(--brand-blue);
    font-weight: 700; color: var(--white);
    font-size: 11px; letter-spacing: 5.6px; white-space: nowrap;
  }

  /* Banner one */
  .banner--one .brand { left: 106px; top: 32px; }
  .accent-band { position: absolute; left: 0; bottom: 0; width: 620px; height: 8px; background: linear-gradient(90deg, var(--brand-blue), var(--deep-blue)); }
  .accent-edge { position: absolute; left: 548px; top: 0; width: 100px; height: 100%; background: var(--brand-blue); clip-path: polygon(62px 0, 100% 0, 17px 100%, 0 100%); }
  .claim-panel { position: absolute; left: 565px; top: 0; width: 492px; height: 100%; background: var(--paper); clip-path: polygon(57px 0, 100% 0, 100% 100%, 0 100%); }
  .claim--condensed {
    position: absolute; right: 36px; top: 8px;
    font-family: "Oswald", sans-serif; font-weight: 400;
    font-size: 57px; line-height: 58px; letter-spacing: -2px;
    color: var(--text-dark); text-align: right; text-transform: uppercase;
    white-space: nowrap;
    transform: scaleX(.85); transform-origin: right top;
  }
  .claim--condensed .figure { color: var(--brand-blue); font-weight: 500; }

  /* Banner two */
  .banner--two .brand { left: 73px; top: 32px; }
  .slash-line { position: absolute; left: 495px; top: 0; width: 80px; height: 100%; background: var(--white); clip-path: polygon(72px 0, 77px 0, 5px 100%, 0 100%); }
  .claim--italic {
    position: absolute; left: 610px; width: 410px; top: 14px;
    font-style: italic; font-weight: 500;
    font-size: 35px; line-height: 52px; letter-spacing: -1.5px;
    color: var(--white); text-align: center; white-space: nowrap;
  }
  .claim--italic .figure {
    font-size: 48px; font-weight: 600; letter-spacing: -2px;
    background: linear-gradient(180deg, #e8f6ff 0%, #5fc2f5 55%, #2a8fd4 100%);
    -webkit-background-clip: text; background-clip: text; color: transparent;
  }

  /* Banner three */
  .banner--three .brand { left: 103px; top: 38px; gap: 14px; }
  .banner--three .brand__mark { width: 58px; height: 58px; }
  .banner--three .brand__name { font-size: 27px; }
  .banner--three .brand__tagline { font-size: 10px; letter-spacing: 4.6px; margin-top: 6px; padding-top: 4px; }
  .divider { position: absolute; left: 507px; top: 27px; width: 2px; height: 77px; background: var(--brand-blue); }
  .claim--plain {
    position: absolute; left: 617px; top: 31px;
    font-weight: 600; font-size: 30px; line-height: 36px;
    color: var(--white); text-transform: uppercase; white-space: nowrap;
  }
  .claim--plain .figure { color: var(--brand-blue); }

  /* Banner four */
  .banner--four .brand { left: 78px; top: 35px; }
  .stat { position: absolute; font-family: "Oswald", sans-serif; font-weight: 600; letter-spacing: -3px; line-height: 1;
    background: linear-gradient(180deg, #f2f9ff 0%, #8fd2f7 45%, #1c8cd6 100%);
    -webkit-background-clip: text; background-clip: text; color: transparent; white-space: nowrap; }
  .stat--papers { left: 509px; top: 14px; font-size: 88px; transform: scaleX(.88); transform-origin: left top; }
  .stat--companies { left: 926px; top: 26px; font-size: 60px; }
  .stat-label { position: absolute; font-family: "Oswald", sans-serif; font-weight: 500; color: var(--white); text-transform: uppercase; white-space: nowrap; line-height: 1; }
  .stat-label--papers { left: 708px; top: 29px; font-size: 33px; letter-spacing: 1.4px; }
  .stat-label--from { left: 767px; top: 63px; font-size: 33px; letter-spacing: 2px; }
  .stat-label--companies { left: 929px; top: 90px; font-family: "Montserrat", sans-serif; font-weight: 600; font-size: 12px; }
  .chevrons { position: absolute; top: 76px; display: flex; gap: 3px; }
  .chevrons--before { left: 716px; }
  .chevrons--after { left: 879px; }
  .chevrons svg { width: 9px; height: 12px; }
</style>
</head>
<body>

<section class="banner banner--one" aria-label="Header banner variation 1">
  <div class="tech-texture" role="img" aria-label="Subtle circuit board texture"></div>
  <div class="accent-band"></div>
  <div class="accent-edge"></div>
  <div class="claim-panel"></div>
  <div class="brand">
    <span class="brand__mark"></span>
    <div class="brand__text">
      <span class="brand__name">VARNEL BRIX</span>
      <span class="brand__tagline">FOR IT PROFESSIONALS</span>
    </div>
  </div>
  <p class="claim--condensed"><span class="figure">11,322</span>&nbsp; Whitepapers<br>From <span class="figure">726</span> Companies</p>
</section>

<section class="banner banner--two" aria-label="Header banner variation 2">
  <div class="tech-texture" role="img" aria-label="Subtle circuit board texture"></div>
  <div class="slash-line"></div>
  <div class="brand">
    <span class="brand__mark"></span>
    <div class="brand__text">
      <span class="brand__name">VARNEL BRIX</span>
      <span class="brand__tagline">FOR IT PROFESSIONALS</span>
    </div>
  </div>
  <p class="claim--italic"><span class="figure">11,322</span> Whitepapers<br>From <span class="figure">726</span> Companies</p>
</section>

<section class="banner banner--three" aria-label="Header banner variation 3">
  <div class="brand">
    <span class="brand__mark"></span>
    <div class="brand__text">
      <span class="brand__name">VARNEL BRIX</span>
      <span class="brand__tagline">FOR IT PROFESSIONALS</span>
    </div>
  </div>
  <div class="divider"></div>
  <p class="claim--plain"><span class="figure">11,322</span> Whitepapers<br>From <span class="figure">726</span> Companies</p>
</section>

<section class="banner banner--four" aria-label="Header banner variation 4">
  <div class="brand">
    <span class="brand__mark"></span>
    <div class="brand__text">
      <span class="brand__name">VARNEL BRIX</span>
      <span class="brand__tagline">FOR IT PROFESSIONALS</span>
    </div>
  </div>
  <span class="stat stat--papers">11,322</span>
  <span class="stat-label stat-label--papers">Whitepapers</span>
  <span class="chevrons chevrons--before">
    <svg viewBox="0 0 9 12"><path d="M1 1 L7 6 L1 11" fill="none" stroke="#1a9ee0" stroke-width="2.2"/></svg>
    <svg viewBox="0 0 9 12"><path d="M1 1 L7 6 L1 11" fill="none" stroke="#1a9ee0" stroke-width="2.2"/></svg>
    <svg viewBox="0 0 9 12"><path d="M1 1 L7 6 L1 11" fill="none" stroke="#1a9ee0" stroke-width="2.2"/></svg>
  </span>
  <span class="stat-label stat-label--from">From</span>
  <span class="chevrons chevrons--after">
    <svg viewBox="0 0 9 12"><path d="M1 1 L7 6 L1 11" fill="none" stroke="#1a9ee0" stroke-width="2.2"/></svg>
    <svg viewBox="0 0 9 12"><path d="M1 1 L7 6 L1 11" fill="none" stroke="#1a9ee0" stroke-width="2.2"/></svg>
    <svg viewBox="0 0 9 12"><path d="M1 1 L7 6 L1 11" fill="none" stroke="#1a9ee0" stroke-width="2.2"/></svg>
  </span>
  <span class="stat stat--companies">726</span>
  <span class="stat-label stat-label--companies">COMPANIES</span>
</section>

</body>
</html>
```